Harrowgate Construction And Masonry Ltd

Black background

Logo - attached

Services (bullet points)
New Builds
Extensions
Refurbishments
Alterations
Brickwork Specialists

Contact details - 01632 960418 or 0791 5530274

Email address - contact@harrowgateconstructionandmasonry.co.uk

Website - www.harrowgateconstructionandmasonry.co.uk

Facebook logo

```html
<!DOCTYPE html>
<html lang="en">
<head>
<meta charset="utf-8">
<title>Harrowgate Construction And Masonry Ltd – Flyer</title>
<link rel="stylesheet" href="https://fonts.googleapis.com/css2?family=Poppins:ital,wght@0,400;0,500;0,600;0,700;1,700&display=swap">
<style>
  :root {
    --stage: #c3c3c3;
    --ink: #000000;
    --green: #43b96a;
    --green-bright: #5fe08a;
    --green-pale: #c9ffd9;
    --white: #ffffff;
    --brick: #2a2a2a;
  }
  * { margin: 0; padding: 0; box-sizing: border-box; }
  html, body {
    width: 1200px; height: 2192px; overflow: hidden;
    background: var(--stage);
    font-family: "Poppins", sans-serif;
  }
  .flyer {
    position: absolute; left: 50px; top: 384px;
    width: 1100px; height: 1424px;
    background: var(--ink);
    overflow: hidden;
    box-shadow: 0 18px 40px rgba(0,0,0,.35);
  }
  .wall {
    position: absolute; left: 0; top: 690px; width: 100%; height: 734px;
    background: linear-gradient(to bottom,
      rgba(42,42,42,0) 0%, var(--brick) 18%, #262626 60%, #1d2a21 75%, #2f8a4f 88%, var(--green) 100%);
  }
  .footer-band {
    position: absolute; left: 0; bottom: 0; width: 100%; height: 300px;
    background: linear-gradient(to bottom, rgba(67,185,106,0) 0%, var(--green) 55%);
  }
  .brand {
    position: absolute; left: 90px; top: 130px; width: 360px;
    display: flex; align-items: flex-start; gap: 18px;
  }
  .brand-mark { width: 44px; height: 44px; background: var(--green); flex: none; margin-top: 6px; }
  .brand-name {
    color: var(--green); font-weight: 600; font-size: 34px; line-height: 1.2;
    text-transform: uppercase; letter-spacing: 1px;
  }
  .headline {
    position: absolute; left: 498px; top: 92px;
    font-size: 74px; line-height: 76px; font-weight: 700; color: var(--green);
  }
  .headline .light { font-weight: 500; }
  .headline .accent { color: var(--white); font-style: italic; display: block; }
  .services-map { position: absolute; left: 0; top: 0; }
  .service-label {
    position: absolute; width: 240px; margin-left: -120px;
    text-align: center; color: var(--white); font-size: 29px; line-height: 36px;
    transform: translateY(-50%);
  }
  .service-label.title { color: #0b1a10; font-size: 52px; line-height: 60px; font-weight: 500; }
  .contact {
    position: absolute; left: 0; width: 100%; display: flex;
    justify-content: center; align-items: center; color: var(--white);
  }
  .contact-phone { top: 1196px; font-size: 44px; font-weight: 600; gap: 26px; }
  .contact-phone .sep { font-weight: 400; }
  .contact-email { top: 1256px; font-size: 31px; gap: 24px; }
  .contact-web { top: 1310px; font-size: 22px; color: #0b1a10; gap: 28px; }
  .contact-web .divider { width: 1px; height: 20px; background: #0b1a10; }
  .follow { display: flex; align-items: center; gap: 8px; font-size: 14px; }
  .social-square { width: 18px; height: 18px; background: var(--white); }
  .icon { width: 34px; height: 34px; }
</style>
</head>
<body>
<main class="flyer">
  <div class="wall" role="img" aria-label="Dark brick wall texture fading into green"></div>
  <div class="footer-band"></div>

  <div class="brand">
    <span class="brand-mark"></span>
    <span class="brand-name">Harrowgate Construction And Masonry Ltd</span>
  </div>

  <h1 class="headline">
    Building<br>
    <span class="light">and</span> Brickwork
    <span class="accent">Specialists</span>
  </h1>

  <svg class="services-map" width="1100" height="1100" viewBox="0 0 1100 1100" aria-hidden="true">
    <defs>
      <filter id="glow" x="-30%" y="-30%" width="160%" height="160%">
        <feGaussianBlur stdDeviation="7" result="b"/>
        <feMerge><feMergeNode in="b"/><feMergeNode in="b"/><feMergeNode in="SourceGraphic"/></feMerge>
      </filter>
      <g id="ring">
        <circle r="135" fill="none" stroke="var(--green-bright)" stroke-width="7" stroke-dasharray="790 58" transform="rotate(100)" filter="url(#glow)"/>
        <circle r="135" fill="none" stroke="var(--green-pale)" stroke-width="2" stroke-dasharray="790 58" transform="rotate(100)"/>
      </g>
    </defs>
    <g stroke="var(--green)" stroke-width="2">
      <line x1="367" y1="579" x2="415" y2="579"/>
      <line x1="685" y1="579" x2="732" y2="579"/>
      <line x1="867" y1="714" x2="867" y2="775"/>
      <line x1="367" y1="910" x2="415" y2="910"/>
      <line x1="685" y1="910" x2="732" y2="910"/>
    </g>
    <circle cx="232" cy="579" r="108" fill="var(--green)"/>
    <use href="#ring" x="232" y="579"/>
    <use href="#ring" x="550" y="579"/>
    <use href="#ring" x="867" y="579"/>
    <use href="#ring" x="232" y="910"/>
    <use href="#ring" x="550" y="910"/>
    <use href="#ring" x="867" y="910"/>
  </svg>

  <p class="service-label title" style="left:232px;top:579px">Services</p>
  <p class="service-label" style="left:550px;top:579px">New<br>Builds</p>
  <p class="service-label" style="left:867px;top:579px">Extensions</p>
  <p class="service-label" style="left:232px;top:910px">Refurbishments</p>
  <p class="service-label" style="left:550px;top:910px">Alterations</p>
  <p class="service-label" style="left:867px;top:910px">Brickwork<br>Specialists</p>

  <div class="contact contact-phone">
    <svg class="icon" viewBox="0 0 24 24" aria-hidden="true"><path fill="#0b1a10" d="M6.6 10.8a15.1 15.1 0 0 0 6.6 6.6l2.2-2.2a1 1 0 0 1 1-.25 11.4 11.4 0 0 0 3.6.57 1 1 0 0 1 1 1V20a1 1 0 0 1-1 1A17 17 0 0 1 3 4a1 1 0 0 1 1-1h3.5a1 1 0 0 1 1 1c0 1.25.2 2.45.57 3.57a1 1 0 0 1-.25 1z"/></svg>
    <span>01632 960418</span><span class="sep">|</span><span>0791 5530274</span>
  </div>
  <div class="contact contact-email">
    <svg class="icon" viewBox="0 0 24 24" aria-hidden="true"><path fill="#0b1a10" d="M2 5h20v14H2z"/><path fill="none" stroke="var(--green)" stroke-width="1.5" d="M2 5l10 8 10-8M2 19l7-7M22 19l-7-7"/></svg>
    <span>contact@harrowgateconstructionandmasonry.co.uk</span>
  </div>
  <div class="contact contact-web">
    <span>www.harrowgateconstructionandmasonry.co.uk</span>
    <span class="divider"></span>
    <span class="follow">Follow us: <span class="social-square"></span></span>
  </div>
</main>
</body>
</html>
```